New Business Card Design Project

We are a spa looking to create a professional elegant business card for a spa mainly black and white with a splash of lime green. This card will be two sided - the front side will have an image, the logo, and the spa's information - the back side will have a promotion for new customers - NEW CUSTOMERS $20 OFF

Look and feel: chic, modern, and spa-ish.
Information to be included:
Therapist Name
Therapist specialty
Address: 5147 Marlowe Ave, Beverly Hills CA 90211
Phone: (310) 482-3961

Let me know if you have any questions!

Thank you

```html
<!DOCTYPE html>
<html lang="en">
<head>
<meta charset="utf-8">
<title>Verda Day Spa – Business Card</title>
<link href="https://fonts.googleapis.com/css2?family=Didact+Gothic&family=Mulish:wght@600;700&display=swap" rel="stylesheet">
<style>
  :root {
    --backdrop-center: #2a9a0a;
    --backdrop-edge: #136a05;
    --lime: #5fe12a;
    --lime-dark: #2e8f0c;
    --name-green: #3a9a12;
    --ink: #1a1a1a;
    --white: #ffffff;
    --band: rgba(120, 170, 70, 0.55);
  }
  * { margin: 0; padding: 0; box-sizing: border-box; }
  html, body { width: 1200px; height: 1200px; overflow: hidden; }
  body {
    position: relative;
    background: radial-gradient(ellipse at 50% 45%, var(--backdrop-center) 0%, var(--backdrop-edge) 100%);
    font-family: "Mulish", sans-serif;
  }
  .card {
    position: absolute;
    left: 212px;
    width: 800px;
    height: 445px;
    overflow: hidden;
    box-shadow: 0 12px 28px rgba(0, 0, 0, 0.35);
  }

  /* Promotion side */
  .card--promo { top: 130px; }
  .promo-photo {
    position: absolute; inset: 0;
    background:
      radial-gradient(ellipse 60% 18% at 60% 88%, rgba(255, 200, 120, 0.75), transparent 70%),
      radial-gradient(ellipse 35% 30% at 75% 60%, #efe9dc 0%, transparent 75%),
      radial-gradient(ellipse 20% 35% at 18% 55%, #b9a27d 0%, transparent 75%),
      linear-gradient(180deg, #6d8a3a 0%, #8a7a4c 45%, #4a2e1a 80%, #120a05 100%);
  }
  .promo-band {
    position: absolute; left: 0; right: 0; top: 27px; height: 166px;
    background: var(--band);
  }
  .promo-text {
    position: absolute; left: 0; right: 0; top: 60px;
    text-align: center; color: var(--white);
    font-family: "Didact Gothic", sans-serif;
  }
  .promo-kicker {
    font-size: 30px; letter-spacing: -0.5px; line-height: 1;
    text-shadow: 0 2px 4px rgba(0, 0, 0, 0.45);
  }
  .promo-offer {
    margin-top: 4px;
    font-family: "Mulish", sans-serif; font-weight: 700;
    font-size: 62px; line-height: 1; letter-spacing: -1px;
    color: var(--lime);
    -webkit-text-stroke: 2px #eaffd8;
    text-shadow: 0 3px 5px rgba(0, 0, 0, 0.45);
  }

  /* Contact side */
  .card--contact { top: 641px; background: var(--white); }
  .contact-photo {
    position: absolute; top: 0; bottom: 0; left: 0; width: 520px;
    background:
      linear-gradient(90deg, rgba(255,255,255,0) 0%, rgba(255,255,255,0) 45%, #ffffff 95%),
      radial-gradient(ellipse 45% 30% at 35% 60%, #e7c1ac 0%, transparent 75%),
      radial-gradient(ellipse 50% 15% at 40% 88%, #f4f1ec 0%, transparent 80%),
      linear-gradient(180deg, #5a8e3c 0%, #9cb98a 40%, #b59a84 70%, #e8e3dc 100%);
  }
  .brand {
    position: absolute; left: 560px; width: 200px; top: 92px;
    text-align: center;
    font-weight: 700; font-size: 26px; color: var(--ink);
  }
  .contact {
    position: absolute; right: 75px; top: 228px;
    text-align: right; color: var(--ink);
  }
  .therapist-name { font-weight: 700; font-size: 26px; color: var(--name-green); line-height: 1.1; }
  .therapist-specialty { font-weight: 600; font-size: 15px; margin-top: 6px; }
  .contact-label { font-weight: 600; font-size: 17px; margin-top: 20px; }
  .contact-label + .contact-value { margin-top: 6px; }
  .contact-value { font-weight: 700; font-size: 16px; }
  .contact-value + .contact-label { margin-top: 8px; }
</style>
</head>
<body>
  <section class="card card--promo">
    <div class="promo-photo" role="img" aria-label="Spa still life: stacked stones, rolled white towel, orchid and a row of lit candles"></div>
    <div class="promo-band"></div>
    <div class="promo-text">
      <p class="promo-kicker">NEW CUSTOMERS</p>
      <p class="promo-offer">$20 OFF</p>
    </div>
  </section>

  <section class="card card--contact">
    <div class="contact-photo" role="img" aria-label="Woman relaxing on a towel with a white flower in her hair, candle and greenery behind"></div>
    <p class="brand">Verda Day Spa</p>
    <div class="contact">
      <p class="therapist-name">Marisol Etxeberri</p>
      <p class="therapist-specialty">Therapist specialty</p>
      <p class="contact-label">Address</p>
      <p class="contact-value">5147 Marlowe Ave, Beverly Hills CA 90211</p>
      <p class="contact-label">Phone</p>
      <p class="contact-value">(310) 482-3961</p>
    </div>
  </section>
</body>
</html>
```